Business card, Letterhead and envelope design
Create a business card, letterhead and envelope design for Velmira Solutions
Professional
name
title
address
email@velmira-example.com
www.velmirasolutions-example.com
logo and font
Trifold brochure design we have for inspiration of design. This is for reference only.

```html
<!DOCTYPE html>
<html lang="en">
<head>
<meta charset="utf-8">
<title>Velmira Solutions – Stationery Set</title>
<link href="https://fonts.googleapis.com/css2?family=Arimo:wght@400;700&display=swap" rel="stylesheet">
<style>
  :root{
    --bg:#e9e9ea;
    --paper:#ffffff;
    --navy:#061a4a;
    --blue:#0d4fb8;
    --sky:#3fa0ef;
    --ink:#1b1b1b;
    --label:#1556c4;
    --faint:#eef0f3;
    --card-dark:#0d0d10;
  }
  *{box-sizing:border-box;margin:0;padding:0}
  html,body{width:1200px;height:827px;overflow:hidden;background:var(--bg);font-family:"Arimo",Arial,sans-serif;color:var(--ink)}
  .stage{position:relative;width:1200px;height:827px}
  .defs{position:absolute;width:0;height:0}
  .sheet{position:absolute;background:var(--paper);box-shadow:0 1px 4px rgba(0,0,0,.18);overflow:hidden}
  .swoosh{position:absolute;left:0;top:0;width:100%;display:block}
  .brand{position:absolute;display:flex;align-items:center;gap:10px;color:#fff;font-weight:700;white-space:nowrap}
  .brand-mark{background:linear-gradient(135deg,#2a2f3a,#0b0e16);border:1px solid #4a5a78}
  .ghost-mark{position:absolute;background:var(--faint)}
  .contact{position:absolute;font-size:7px;line-height:1.55;color:var(--ink);white-space:nowrap}
  .contact b{color:var(--label);font-weight:700;display:inline-block;width:30px}

  /* Letterhead */
  .letterhead{left:35px;top:20px;width:455px;height:780px}
  .letterhead .brand{left:28px;top:22px;font-size:22px}
  .letterhead .brand-mark{width:46px;height:46px}
  .letterhead .ghost-mark{left:130px;top:330px;width:200px;height:200px}
  .letter-footer{position:absolute;left:0;right:0;bottom:14px;text-align:center;font-size:6.5px;line-height:1.7}
  .letter-footer b{color:var(--label)}
  .letter-footer .sep{color:var(--label);padding:0 6px}

  /* Business cards */
  .card{width:430px;height:148px;border-radius:8px}
  .card-light{left:625px;top:36px}
  .card-dark{left:815px;top:211px;width:235px;height:120px;background:var(--card-dark)}
  .card-light .brand{left:20px;top:12px;font-size:16px}
  .card-light .brand-mark{width:36px;height:36px}
  .card-light .person{position:absolute;left:22px;top:98px;font-size:15px;color:var(--blue)}
  .card-light .contact{left:215px;top:80px;font-size:7px}
  .card-dark .brand{left:10px;top:7px;font-size:10px;gap:6px}
  .card-dark .brand-mark{width:22px;height:22px}
  .card-dark .person{position:absolute;left:12px;top:70px;font-size:11px;color:#fff}
  .card-dark .contact{left:108px;top:57px;font-size:5.5px;color:#e8e8e8}
  .card-dark .contact b{color:var(--sky);width:20px}

  /* Envelope */
  .envelope{left:508px;top:380px;width:650px;height:393px;overflow:visible;background:transparent;box-shadow:none}
  .env-flap{position:absolute;left:0;top:0;width:650px;height:124px}
  .env-body{position:absolute;left:0;top:122px;width:650px;height:271px;background:var(--paper);box-shadow:0 1px 4px rgba(0,0,0,.18);overflow:hidden}
  .flap-mark{position:absolute;left:307px;top:50px;width:36px;height:36px}
  .env-body .brand{left:20px;top:16px;font-size:21px}
  .env-body .brand-mark{width:46px;height:46px}
  .env-body .contact{left:18px;top:178px}
  .env-body .ghost-mark{left:470px;top:140px;width:130px;height:120px}
</style>
</head>
<body>
<main class="stage">
  <svg class="defs" aria-hidden="true">
    <defs>
      <linearGradient id="band" x1="0" y1="0" x2="1" y2="0.4">
        <stop offset="0" stop-color="#04123a"/>
        <stop offset=".45" stop-color="#0b47ad"/>
        <stop offset=".75" stop-color="#1f7fe0"/>
        <stop offset="1" stop-color="#0a2f80"/>
      </linearGradient>
      <linearGradient id="flap" x1="0" y1="0" x2="0" y2="1">
        <stop offset="0" stop-color="#0a3da0"/>
        <stop offset=".6" stop-color="#1767cf"/>
        <stop offset="1" stop-color="#062364"/>
      </linearGradient>
    </defs>
  </svg>

  <!-- Letterhead -->
  <section class="sheet letterhead" aria-label="Letterhead">
    <svg class="swoosh" viewBox="0 0 400 100" preserveAspectRatio="none" style="height:118px">
      <rect width="400" height="100" fill="url(#band)"/>
      <path d="M0 78 C110 40 250 100 400 42 L400 100 L0 100Z" fill="#fff"/>
      <path d="M0 74 C110 36 250 96 400 38" fill="none" stroke="#0a0a0a" stroke-width="3"/>
      <path d="M0 82 C110 46 250 104 400 48" fill="none" stroke="#59b4f5" stroke-width="1.2"/>
    </svg>
    <div class="brand"><span class="brand-mark"></span>Velmira Solutions</div>
    <div class="ghost-mark" role="img" aria-label="Faint brand mark decoration"></div>
    <div class="letter-footer">
      120 Harbor Lane, Dallas, IL 60601<br>
      <b>Office:</b> 555 010 0142<span class="sep">|</span><b>Fax:</b> 555 010 0143<span class="sep">|</span><b>Email:</b> email@velmira-example.com<span class="sep">|</span><b>Web:</b> www.velmirasolutions-example.com
    </div>
  </section>

  <!-- Business card, light -->
  <section class="sheet card card-light" aria-label="Business card, light">
    <svg class="swoosh" viewBox="0 0 400 100" preserveAspectRatio="none" style="height:100%">
      <path d="M0 0 H400 V32 C320 44 220 30 120 34 C70 36 30 38 0 44Z" fill="url(#band)"/>
      <path d="M0 46 C30 40 70 38 120 36 C220 32 320 46 400 34" fill="none" stroke="#0a0a0a" stroke-width="2.2"/>
      <path d="M0 51 C30 45 70 43 120 41 C220 37 320 51 400 39" fill="none" stroke="#59b4f5" stroke-width="1"/>
    </svg>
    <div class="brand"><span class="brand-mark"></span>Velmira Solutions</div>
    <div class="person">Daniel Hart</div>
    <div class="contact">
      120 Harbor Lane, Dallas, IL 60601<br>
      <b>Office</b> 555 010 0142<br>
      <b>Fax</b> 555 010 0143<br>
      <b>Email</b> email@velmira-example.com<br>
      <b>Web</b> www.velmirasolutions-example.com
    </div>
  </section>

  <!-- Business card, dark -->
  <section class="sheet card card-dark" aria-label="Business card, dark">
    <svg class="swoosh" viewBox="0 0 400 100" preserveAspectRatio="none" style="height:100%">
      <path d="M0 0 H400 V26 C320 36 220 24 120 28 C70 30 30 32 0 36Z" fill="url(#band)"/>
      <path d="M0 38 C30 34 70 32 120 30 C220 26 320 38 400 28" fill="none" stroke="#ffffff" stroke-width="1.6"/>
      <path d="M0 42 C30 38 70 36 120 34 C220 30 320 42 400 32" fill="none" stroke="#59b4f5" stroke-width="1"/>
    </svg>
    <div class="brand"><span class="brand-mark"></span>Velmira Solutions</div>
    <div class="person">Daniel Hart</div>
    <div class="contact">
      120 Harbor Lane, Dallas, IL 60601<br>
      <b>Office</b> 555 010 0142<br>
      <b>Fax</b> 555 010 0143<br>
      <b>Email</b> email@velmira-example.com<br>
      <b>Web</b> www.velmirasolutions-example.com
    </div>
  </section>

  <!-- Envelope -->
  <section class="sheet envelope" aria-label="Envelope">
    <svg class="env-flap" viewBox="0 0 650 124" preserveAspectRatio="none">
      <path d="M0 124 L60 4 Q64 0 70 0 H580 Q586 0 590 4 L650 124Z" fill="url(#flap)"/>
    </svg>
    <span class="brand-mark flap-mark"></span>
    <div class="env-body">
      <svg class="swoosh" viewBox="0 0 400 100" preserveAspectRatio="none" style="height:115px">
        <rect width="400" height="100" fill="url(#band)"/>
        <path d="M0 84 C120 40 260 98 400 40 L400 100 L0 100Z" fill="#fff"/>
        <path d="M0 80 C120 36 260 94 400 36" fill="none" stroke="#0a0a0a" stroke-width="3"/>
        <path d="M0 88 C120 46 260 102 400 46" fill="none" stroke="#59b4f5" stroke-width="1.2"/>
      </svg>
      <div class="brand"><span class="brand-mark"></span>Velmira Solutions</div>
      <div class="ghost-mark" role="img" aria-label="Faint brand mark decoration"></div>
      <div class="contact">
        120 Harbor Lane, Dallas, IL 60601<br>
        <b>Office</b> 555 010 0142<br>
        <b>Fax</b> 555 010 0143<br>
        <b>Email</b> email@velmira-example.com<br>
        <b>Web</b> www.velmirasolutions-example.com
      </div>
    </div>
  </section>
</main>
</body>
</html>
```